Diesel Fitting/Mechanical Company Needs a new Business Card

We would like a new business card that showcases our logo and business information.

Industry/Entity Type

Business

Contact Information for Business Card

314 Wendale Street
PO Box 7581 BRAMLEY DOWNS QLD 4831
Phone: 49312787 Fax: 49312688 Mobile: 0438915276 ABN: 63 519 087 342

Requirements
Must have
• The following email addresses:
• admin@tkservicing.com.au , sales@tkservicing.com.au , accounts@tkservicing.com.au , parts@tkservicing.com.au , office@tkservicing.com.au
• Also need to have the website: www.tkservicing.com.au

```html
<!DOCTYPE html>
<html lang="en">
<head>
<meta charset="utf-8">
<title>TK Servicing – Business Card</title>
<link href="https://fonts.googleapis.com/css2?family=Source+Sans+3:wght@400;600&display=swap" rel="stylesheet">
<style>
  :root{
    --stage-top:#2b2b2b;
    --stage-bottom:#050505;
    --card:#ffffff;
    --ink:#1f1f1f;
    --accent:#e02127;
    --brand:#ef6a1f;
  }
  *{margin:0;padding:0;box-sizing:border-box}
  html,body{width:1200px;height:900px;overflow:hidden}
  body{
    background:linear-gradient(180deg,var(--stage-top) 0%,#1a1a1a 45%,var(--stage-bottom) 100%);
    font-family:"Source Sans 3",sans-serif;
    color:var(--ink);
    position:relative;
  }
  .card{
    position:absolute;top:306px;width:440px;height:271px;
    background:var(--card);border-radius:12px;
  }
  .card--front{left:149px}
  .card--back{left:608px}

  .brand{
    position:absolute;left:0;right:0;top:54px;
    display:flex;justify-content:center;align-items:center;gap:10px;
  }
  .brand__dot{width:18px;height:18px;border-radius:50%;background:var(--brand)}
  .brand__name{font-size:30px;font-weight:600;color:var(--brand);letter-spacing:.5px}

  .contact{font-size:12.5px;line-height:16px;position:absolute;white-space:nowrap}
  .phones{right:215px;top:144px;text-align:right}
  .phones li,.emails li{list-style:none;display:flex;align-items:center;height:16px}
  .phones li{justify-content:flex-end;gap:7px}
  .icon{width:9px;height:9px;fill:var(--accent);flex:none}
  .abn{right:214px;top:196px;text-align:right}
  .abn__label{color:var(--accent)}
  .address{right:215px;top:217px;text-align:right}

  .emails{left:241px;top:152px}
  .emails li{gap:6px}
  .web-domain{color:var(--accent)}
</style>
</head>
<body>
  <section class="card card--front" aria-label="Business card front">
    <div class="brand">
      <span class="brand__dot"></span>
      <span class="brand__name">TK Servicing</span>
    </div>

    <ul class="contact phones">
      <li><span>0438915276</span>
        <svg class="icon" viewBox="0 0 10 10"><rect x="2.5" y="0" width="5" height="10" rx="1"/><rect x="3.5" y="1.2" width="3" height="6" fill="#fff"/></svg></li>
      <li><span>49312787</span>
        <svg class="icon" viewBox="0 0 10 10"><path d="M0 3 Q5 0 10 3 L9 4.5 L7 3.8 L6.5 3 H3.5 L3 3.8 L1 4.5Z"/><rect x="2" y="5" width="6" height="4" rx="1"/></svg></li>
      <li><span>49312688</span>
        <svg class="icon" viewBox="0 0 10 10"><rect x="2.5" y="0" width="5" height="3"/><rect x="0.5" y="3" width="9" height="6" rx="1"/><rect x="2.5" y="5" width="5" height="2" fill="#fff"/></svg></li>
    </ul>

    <p class="contact abn"><span class="abn__label">ABN:</span> 63 519 087 342</p>

    <p class="contact address">314 Wendale Street PO Box 7581<br>BRAMLEY DOWNS QLD 4831</p>

    <ul class="contact emails">
      <li><svg class="icon" viewBox="0 0 10 10"><circle cx="5" cy="5" r="5"/><path d="M2 3.5 L4.5 4 L4 6.5 L5.5 8 M6 1.5 L7 3.5 L8.5 4" stroke="#fff" stroke-width="1" fill="none"/></svg><span>admin@tkservicing.com.au</span></li>
      <li><svg class="icon" viewBox="0 0 10 10"><circle cx="5" cy="5" r="5"/><path d="M2 3.5 L4.5 4 L4 6.5 L5.5 8 M6 1.5 L7 3.5 L8.5 4" stroke="#fff" stroke-width="1" fill="none"/></svg><span>sales@tkservicing.com.au</span></li>
      <li><svg class="icon" viewBox="0 0 10 10"><circle cx="5" cy="5" r="5"/><path d="M2 3.5 L4.5 4 L4 6.5 L5.5 8 M6 1.5 L7 3.5 L8.5 4" stroke="#fff" stroke-width="1" fill="none"/></svg><span>accounts@tkservicing.com.au</span></li>
      <li><svg class="icon" viewBox="0 0 10 10"><circle cx="5" cy="5" r="5"/><path d="M2 3.5 L4.5 4 L4 6.5 L5.5 8 M6 1.5 L7 3.5 L8.5 4" stroke="#fff" stroke-width="1" fill="none"/></svg><span>parts@tkservicing.com.au</span></li>
      <li><svg class="icon" viewBox="0 0 10 10"><circle cx="5" cy="5" r="5"/><path d="M2 3.5 L4.5 4 L4 6.5 L5.5 8 M6 1.5 L7 3.5 L8.5 4" stroke="#fff" stroke-width="1" fill="none"/></svg><span>office@tkservicing.com.au</span></li>
      <li><svg class="icon" viewBox="0 0 10 10"><circle cx="5" cy="5" r="5"/><path d="M2 3.5 L4.5 4 L4 6.5 L5.5 8 M6 1.5 L7 3.5 L8.5 4" stroke="#fff" stroke-width="1" fill="none"/></svg><span>www.<span class="web-domain">tkservicing.com</span>.au</span></li>
    </ul>
  </section>

  <section class="card card--back" aria-label="Business card back"></section>
</body>
</html>
```